Harborline Stay Collective Business Card Design

Design a business card for Harborline Stay Collective. Look at the website for colors and reference. Card should have logo, name, title, office number, mobile number, email, URL and a tagline like, "Luxury Hotel & Resort Email Marketing" (This might change).

https://www.harborlinestaycollective.net

The rest I will leave up to your imagination.

Contact Information for Business Card

Logo, name, title, office number, mobile number, email, URL and a tagline like, "Luxury Hotel & Resort Email Marketing" (This might change).

```html
<!DOCTYPE html>
<html lang="en">
<head>
<meta charset="utf-8">
<title>Harborline Stay Collective – Business Card</title>
<link rel="stylesheet" href="https://fonts.googleapis.com/css2?family=Krona+One&family=Ubuntu:wght@400;700&display=swap">
<style>
  :root {
    --bg: #9a9a9a;
    --black: #000000;
    --white: #ffffff;
    --orange: #f77200;
    --ink: #111111;
  }
  * { box-sizing: border-box; margin: 0; padding: 0; }
  html, body { width: 1093px; height: 1200px; overflow: hidden; }
  body {
    background: var(--bg);
    position: relative;
    font-family: "Ubuntu", sans-serif;
  }
  .card {
    position: absolute;
    left: 264px;
    width: 580px;
    height: 357px;
    overflow: hidden;
  }

  /* Front */
  .card--front { top: 226px; background: var(--white); }
  .front__bar {
    position: absolute; left: 0; top: 0; bottom: 0; width: 58px;
    background: var(--black);
  }
  .front__rule {
    position: absolute; left: 58px; top: 0; bottom: 0; width: 7px;
    background: var(--orange);
  }
  .brand {
    position: absolute;
    display: flex; align-items: center; gap: 9px;
    font-weight: 700;
    text-transform: uppercase;
    white-space: nowrap;
  }
  .brand__mark { width: 12px; height: 12px; background: var(--orange); flex: none; }
  .card--front .brand {
    right: 40px; top: 74px;
    font-size: 18px; letter-spacing: 0.5px; color: var(--ink);
  }
  .person { position: absolute; left: 99px; top: 176px; }
  .person__name {
    font-family: "Krona One", sans-serif;
    font-size: 16px; letter-spacing: 0.6px;
    color: var(--ink); line-height: 1;
    text-transform: uppercase;
  }
  .person__title {
    margin-top: 5px;
    font-size: 16px; color: var(--orange); letter-spacing: 0.3px;
  }
  .contacts {
    position: absolute; left: 99px; top: 236px;
    list-style: none;
  }
  .contacts__item {
    display: flex; align-items: center;
    height: 21px;
    font-size: 16px; color: var(--ink); letter-spacing: 0.4px;
  }
  .contacts__icon { width: 15px; height: 15px; margin-right: 7px; flex: none; }
  .contacts__accent { color: var(--orange); }

  /* Back */
  .card--back { top: 620px; background: var(--black); }
  .card--back .brand {
    left: 0; right: 0; top: 156px; justify-content: center;
    font-size: 24px; letter-spacing: 1px; color: var(--white);
  }
  .card--back .brand__mark { width: 15px; height: 15px; }
  .tagline-band {
    position: absolute; left: 0; right: 0; top: 275px; height: 42px;
    background: var(--orange);
    display: flex; align-items: center; justify-content: center;
    font-size: 16.5px; color: var(--white); letter-spacing: 0.3px;
  }
</style>
</head>
<body>

<section class="card card--front" aria-label="Business card front">
  <div class="front__bar"></div>
  <div class="front__rule"></div>

  <div class="brand"><span class="brand__mark"></span>Harborline Stay Collective</div>

  <div class="person">
    <p class="person__name">Marcus Ellery</p>
    <p class="person__title">Managing Director</p>
  </div>

  <ul class="contacts">
    <li class="contacts__item">
      <svg class="contacts__icon" viewBox="0 0 16 16" aria-hidden="true">
        <path d="M3.5 1.5l2.3 2.6-1.2 1.8c.8 1.9 2.2 3.3 4.1 4.2l1.8-1.2 2.6 2.3-1.5 2.1C6.5 13 2.8 9.4 1.4 3.2z" fill="#f77200"/>
        <path d="M9.5 1.5a5 5 0 0 1 5 5M9.5 4a2.5 2.5 0 0 1 2.5 2.5" stroke="#f77200" stroke-width="1.4" fill="none"/>
      </svg>044-318 227 604
    </li>
    <li class="contacts__item">
      <svg class="contacts__icon" viewBox="0 0 16 16" aria-hidden="true">
        <rect x="3.5" y="0.8" width="9" height="14.4" rx="1.5" stroke="#f77200" stroke-width="1.4" fill="none"/>
        <circle cx="8" cy="12.6" r="0.9" fill="#f77200"/>
      </svg>044-318 227 604
    </li>
    <li class="contacts__item">
      <svg class="contacts__icon" viewBox="0 0 16 16" aria-hidden="true">
        <rect x="0.5" y="3" width="15" height="10.5" fill="#f77200"/>
        <path d="M0.5 3.5L8 9l7.5-5.5M0.5 13l5.5-5M15.5 13L10 8" stroke="#fff" stroke-width="1" fill="none"/>
      </svg>hello@harborlinestay.net
    </li>
    <li class="contacts__item">
      <svg class="contacts__icon" viewBox="0 0 16 16" aria-hidden="true">
        <circle cx="8" cy="8" r="7" fill="#f77200"/>
        <path d="M1 8h14M8 1v14M2.5 4.5h11M2.5 11.5h11M8 1c-3 3.5-3 10.5 0 14M8 1c3 3.5 3 10.5 0 14" stroke="#fff" stroke-width="0.9" fill="none"/>
      </svg>www.<span class="contacts__accent">harborlinestaycollective</span>.net
    </li>
  </ul>
</section>

<section class="card card--back" aria-label="Business card back">
  <div class="brand"><span class="brand__mark"></span>Harborline Stay Collective</div>
  <div class="tagline-band">Luxury Hotel &amp; Resort Email Marketing</div>
</section>

</body>
</html>
```